Online Psychology Practice needs business cards.

Online Psychology service needs business cards. Have own logo- please see uploaded. I have other file formats if you need (not sure one needed?)

Details for Business Card:
Fiona Kettlewood
Clinical Psychologist BPsych, BPsych (Hons), MPsych (Clin), MAPS
T: 0457260714 | F: 08 71526804
E: hello@harbourlightmindcarestudio.com.au
W: harbourlightmindcarestudio.com.au

Industry/Entity Type

Health

Contact Information for Business Card

Logo plus details above (couldn't write in this section)

```html
<!DOCTYPE html>
<html lang="en">
<head>
<meta charset="utf-8">
<title>Harbourlight Mindcare Studio – Business Cards</title>
<link rel="stylesheet" href="https://fonts.googleapis.com/css2?family=Open+Sans:wght@400;600;700&display=swap">
<style>
  :root {
    --backdrop: #222223;
    --card: #ffffff;
    --navy: #1d5a87;
    --teal: #168fae;
    --ink: #1c1c1c;
    --radius: 26px;
  }
  * { box-sizing: border-box; margin: 0; padding: 0; }
  html, body { width: 1200px; height: 988px; overflow: hidden; }
  body {
    background: var(--backdrop);
    font-family: "Open Sans", Arial, sans-serif;
    display: flex;
    flex-direction: column;
    align-items: center;
    justify-content: center;
    gap: 40px;
  }
  .card {
    position: relative;
    width: 760px;
    height: 434px;
    background: var(--card);
    border-radius: var(--radius);
    overflow: hidden;
  }

  /* Front */
  .front .wordmark {
    position: absolute;
    left: 0; right: 0; top: 0; bottom: 0;
    display: flex;
    flex-direction: column;
    align-items: center;
    justify-content: center;
    gap: 22px;
  }
  .wordmark-dot {
    width: 64px; height: 64px;
    border-radius: 50%;
    background: var(--teal);
  }
  .wordmark-name {
    font-weight: 600;
    font-size: 34px;
    letter-spacing: 1px;
    color: var(--navy);
    text-align: center;
    line-height: 1.15;
  }

  /* Back */
  .back .brand {
    position: absolute;
    left: 56px; top: 58px;
    display: flex;
    align-items: center;
    gap: 14px;
  }
  .back .brand .wordmark-dot { width: 34px; height: 34px; }
  .back .brand .wordmark-name { font-size: 24px; text-align: left; }
  .feature-disc {
    position: absolute;
    right: 52px; top: 52px;
    width: 250px; height: 250px;
    border-radius: 50%;
    background: var(--teal);
  }
  .tab {
    position: absolute;
    left: -10px; top: 196px;
    width: 28px; height: 76px;
    border-radius: 10px;
    background: var(--navy);
  }
  .person {
    position: absolute;
    left: 56px; top: 188px;
  }
  .person-name {
    font-weight: 700;
    font-size: 34px;
    color: var(--navy);
    line-height: 1.1;
  }
  .person-role {
    font-size: 16px;
    color: var(--ink);
    line-height: 1.35;
    margin-top: 6px;
  }
  .contacts {
    position: absolute;
    left: 70px; top: 300px;
    list-style: none;
    font-size: 16px;
    color: var(--ink);
    line-height: 1;
  }
  .contacts li {
    display: flex;
    align-items: center;
    gap: 10px;
    height: 26px;
  }
  .contacts svg { width: 14px; height: 14px; fill: var(--navy); flex: none; }
</style>
</head>
<body>

  <section class="card front">
    <div class="wordmark">
      <span class="wordmark-dot"></span>
      <span class="wordmark-name">Harbourlight<br>Mindcare Studio</span>
    </div>
  </section>

  <section class="card back">
    <div class="brand">
      <span class="wordmark-dot"></span>
      <span class="wordmark-name">Harbourlight Mindcare Studio</span>
    </div>
    <div class="feature-disc"></div>
    <div class="tab"></div>

    <div class="person">
      <h1 class="person-name">Fiona Kettlewood</h1>
      <p class="person-role">Clinical Psychologist BPsych,<br>BPsych (Hons), MPsych (Clin), MAPS</p>
    </div>

    <ul class="contacts">
      <li>
        <svg viewBox="0 0 24 24"><path d="M6.6 10.8a15.1 15.1 0 0 0 6.6 6.6l2.2-2.2a1 1 0 0 1 1-.25 11.4 11.4 0 0 0 3.6.57 1 1 0 0 1 1 1V20a1 1 0 0 1-1 1A17 17 0 0 1 3 4a1 1 0 0 1 1-1h3.5a1 1 0 0 1 1 1c0 1.25.2 2.45.57 3.57a1 1 0 0 1-.25 1z"/></svg>
        0457260714
      </li>
      <li>
        <svg viewBox="0 0 24 24"><path d="M6 2h9l3 3v4H6z M3 10h18v8h-3v4H6v-4H3z M8 15v5h8v-5z"/></svg>
        08 71526804
      </li>
      <li>
        <svg viewBox="0 0 24 24"><path d="M2 5h20v14H2z M4 7v.5l8 5.5 8-5.5V7l-8 5.5z" fill-rule="evenodd"/></svg>
        hello@harbourlightmindcarestudio.com.au
      </li>
      <li>
        <svg viewBox="0 0 24 24"><path d="M12 2a10 10 0 1 0 0 20 10 10 0 0 0 0-20zm0 2c1 1.4 1.8 3.3 2 5h-4c.2-1.7 1-3.6 2-5zM4.3 13a8 8 0 0 1 0-2H8v2zm1 2H8c.3 1.4.8 2.7 1.4 3.6A8 8 0 0 1 5.3 15zM10 13v-2h4v2zm2 7c-1-1.4-1.7-3.2-2-5h4c-.3 1.8-1 3.6-2 5zm2.6-1.4c.6-.9 1.1-2.2 1.4-3.6h2.7a8 8 0 0 1-4.1 3.6zM16 13v-2h3.7a8 8 0 0 1 0 2z"/></svg>
        www.harbourlightmindcarestudio.com.au
      </li>
    </ul>
  </section>

</body>
</html>
```